Business Card Design Project

I need a cool business card design for the company that will build residential houses.
The card should include:
1) Name: Borek Valdisov
2) Cell: 587.244.XXXX
3) Email: bor.valdisov@qorvina.example
4) Position: General Manager
5) Residential Home Building
6) Company logo that I have uploaded

Industry/Entity Type

Residential

```html
<!DOCTYPE html>
<html lang="en">
<head>
<meta charset="utf-8">
<title>Qorvina Developments – Business Card</title>
<link href="https://fonts.googleapis.com/css2?family=Oswald:wght@500&family=Roboto:wght@400;700&family=Ubuntu:wght@500&display=swap" rel="stylesheet">
<style>
  :root {
    --stage: #2b2c2e;
    --paper: #ffffff;
    --green: #7ed321;
    --blue: #3a8fdc;
    --sky: #4fc6f2;
    --charcoal: #2f3336;
    --ink: #3c4043;
    --muted: #6c7075;
  }
  * { margin: 0; padding: 0; box-sizing: border-box; }
  html, body { width: 1200px; height: 900px; overflow: hidden; background: var(--stage); }
  .stage {
    width: 1200px; height: 900px;
    display: flex; flex-direction: column; align-items: center; justify-content: center; gap: 40px;
  }
  .card {
    position: relative; width: 620px; height: 354px;
    background: var(--paper); overflow: hidden;
    box-shadow: 0 8px 24px rgba(0,0,0,.45);
  }

  /* Front */
  .front .band { position: absolute; left: 0; right: 0; }
  .front .band-green-top { top: 0; height: 18px; background: var(--green); }
  .front .band-blue-top { top: 22px; height: 6px; background: var(--blue); }
  .front .band-green-bottom { bottom: 30px; height: 6px; background: var(--green); }
  .front .band-blue-bottom { bottom: 0; height: 26px; background: var(--blue); }
  .front .identity {
    position: absolute; left: 70px; top: 120px;
    font-family: "Ubuntu", sans-serif; font-weight: 500;
  }
  .front .company-name {
    display: flex; align-items: center; gap: 12px;
    color: var(--blue); font-size: 30px; letter-spacing: 1px;
  }
  .front .company-mark { width: 22px; height: 22px; background: var(--green); }
  .front .tagline {
    margin-top: 18px; margin-left: 40px;
    color: var(--ink); font-size: 36px; letter-spacing: .5px;
  }

  /* Back */
  .back .title-band {
    position: absolute; left: 0; top: 72px; width: 440px; height: 52px;
    background: var(--sky);
  }
  .back .corner-square {
    position: absolute; left: 525px; top: 22px; width: 78px; height: 50px; background: var(--sky);
  }
  .back .title {
    position: absolute; right: 22px; top: 78px;
    font-family: "Oswald", sans-serif; font-weight: 500; font-size: 32px; letter-spacing: 1px;
    color: var(--paper); line-height: 40px;
  }
  .back .title .accent { color: var(--green); }
  .back .rule { position: absolute; height: 3px; background: var(--sky); }
  .back .rule-upper { left: 150px; right: 0; top: 218px; }
  .back .rule-lower { left: 150px; right: 0; top: 268px; }
  .back .dark-strip {
    position: absolute; left: 0; right: 0; top: 274px; bottom: 0; background: var(--charcoal);
  }
  .back .person {
    position: absolute; left: 160px; top: 186px;
    font-family: "Roboto", sans-serif; color: var(--ink);
  }
  .back .person-name { font-weight: 700; font-size: 19px; letter-spacing: .5px; }
  .back .person-role { font-size: 13px; color: var(--muted); margin-left: 8px; }
  .back .contact {
    position: absolute; left: 172px; top: 234px; display: flex; gap: 44px;
    font-family: "Roboto", sans-serif; font-size: 13px; color: var(--muted);
  }
  .back .contact .label { margin-right: 8px; color: var(--ink); }
  .back .logo-box {
    position: absolute; left: 36px; top: 180px; width: 104px; height: 104px;
    background: var(--paper); border: 5px solid var(--sky);
    display: flex; align-items: center; justify-content: center;
    font-family: "Ubuntu", sans-serif; font-weight: 500; font-size: 17px; color: var(--blue);
  }
</style>
</head>
<body>
<main class="stage">
  <section class="card front" aria-label="Card front">
    <div class="band band-green-top"></div>
    <div class="band band-blue-top"></div>
    <div class="identity">
      <div class="company-name"><span class="company-mark"></span>Qorvina Developments</div>
      <div class="tagline">Residential Home Building</div>
    </div>
    <div class="band band-green-bottom"></div>
    <div class="band band-blue-bottom"></div>
  </section>

  <section class="card back" aria-label="Card back">
    <div class="title-band"></div>
    <div class="corner-square"></div>
    <div class="title">RESIDENTIAL <span class="accent">HOME BUILDING</span></div>
    <div class="rule rule-upper"></div>
    <div class="person">
      <span class="person-name">BOREK VALDISOV</span><span class="person-role">General Manager</span>
    </div>
    <div class="contact">
      <span><span class="label">[ T ]</span>587.244.XXXX</span>
      <span><span class="label">[ E ]</span>bor.valdisov@qorvina.example</span>
    </div>
    <div class="rule rule-lower"></div>
    <div class="dark-strip"></div>
    <div class="logo-box">Qorvina</div>
  </section>
</main>
</body>
</html>
```